Invitation for end of year celebration and moving up ceremony/graduatio

Create an invitation template to be used for a fifth grade moving up end of year event. The theme for the event is sports and we will be using a graphic like the attached.

Details subject to change but current details to be included on event are as follows:
Event Date June 12, 2020 6 PM - 9:15 PM
Fifth Graders arrive 6PM
Parents arrive 8:30 PM for family photos and video presentation
Event Name: Maple Crest Falcon Trials
You are invited to Maple Crest Stadium for the Falcon Trials!

Uploaded file includes a sample from a prior year's event (Pinecone file). and the graphic logo to be included on the event this year.

Target Market(s)

11 year old boys and girls and their parents. The event is to celebrate the children's last year at their elementary school as they move up to middle school. (Grade 6).

Industry/Entity Type

School

Colors
0456a4
0792cd
ffffff
fbee3e
ec1f27

Requirements
Must have
• include 1 or 2 of the graphics attached - at least 1 must be a stadium graphic.
• Invitation will be printed on approximately 8x4 or 9x4 card stock for ticket like invites. so the file needs to be created in a way that will allow adjusting for printing/bleedlines and cut lines.
Nice to have
• Some ideas I would like to see are to make it look like a ticket for a sporting event .

```html
<!DOCTYPE html>
<html lang="en">
<head>
<meta charset="utf-8">
<title>Maple Crest Falcon Trials – Invitation</title>
<link rel="stylesheet" href="https://fonts.googleapis.com/css2?family=Alfa+Slab+One&family=Lobster+Two:ital,wght@1,700&display=swap">
<style>
  :root{
    --navy:#0b4a8f;
    --yellow:#ffe000;
    --green:#11a04a;
    --white:#ffffff;
    --art-warm:#d9a07a;
    --art-cool:#8aa6d6;
  }
  *{margin:0;padding:0;box-sizing:border-box}
  html,body{width:805px;height:1200px;overflow:hidden;background:var(--white)}
  .canvas{position:relative;width:805px;height:1200px;background:var(--white)}
  .ticket-border{position:absolute;left:72px;top:73px;width:674px;height:1066px;background:var(--yellow)}
  .ticket-frame{position:absolute;left:107px;top:105px;width:603px;height:1003px;background:var(--navy);border-radius:48px}
  .ticket-body{position:absolute;left:116px;top:168px;width:586px;height:932px;background:var(--white);border-radius:0 0 40px 40px}
  .invite-heading{position:absolute;left:107px;top:113px;width:603px;text-align:center;font-family:"Alfa Slab One",serif;font-weight:400;font-size:32px;letter-spacing:2px;color:var(--white)}
  .stadium-art{position:absolute;left:178px;top:270px;width:474px;height:252px;border-radius:40px 40px 20px 20px;
    background:radial-gradient(ellipse at 50% 45%, #b8323a 0%, var(--art-warm) 45%, var(--art-cool) 75%, #ffffff 100%)}
  .decor{position:absolute;left:0;top:0;width:805px;height:1200px}
  .tagline{position:absolute;left:141px;top:641px;width:536px;height:52px;border-top:3px solid var(--navy);border-bottom:3px solid var(--navy);
    font-family:"Alfa Slab One",serif;font-size:24.5px;color:var(--green);text-align:center;line-height:46px;white-space:nowrap}
  .event-date{position:absolute;left:146px;top:714px;width:220px;text-align:center;font-family:"Alfa Slab One",serif;color:var(--navy)}
  .event-date .day{display:block;font-size:45px;line-height:54px;letter-spacing:-1.5px}
  .event-date .year{display:block;font-size:58px;line-height:64px;color:var(--green);letter-spacing:-1px}
  .year-arrow{position:absolute;top:785px;width:0;height:0;border-top:17px solid transparent;border-bottom:17px solid transparent}
  .year-arrow.left{left:146px;border-left:17px solid var(--green)}
  .year-arrow.right{left:346px;border-right:17px solid var(--green)}
  .event-time{position:absolute;left:380px;top:726px;width:293px;height:98px;background:var(--navy);
    font-family:"Alfa Slab One",serif;font-size:30px;color:var(--white);text-align:center;line-height:98px;white-space:nowrap}
  .arrival-banner{position:absolute;left:134px;top:847px;width:550px;height:55px;background:var(--green);
    clip-path:polygon(0 0,100% 0,97% 50%,100% 100%,0 100%,3% 50%);
    font-family:"Alfa Slab One",serif;font-size:28px;color:var(--white);text-align:center;line-height:57px;letter-spacing:.5px;white-space:nowrap}
  .parent-note{position:absolute;left:126px;top:914px;width:566px;text-align:center;font-family:"Alfa Slab One",serif;font-size:23px;line-height:39px;color:var(--navy);white-space:nowrap}
  .admit-one{position:absolute;left:290px;top:1020px;width:240px;text-align:center;font-family:"Alfa Slab One",serif;font-size:31px;color:var(--green);letter-spacing:.5px}
  .sports-art{position:absolute;top:1000px;width:118px;height:89px;border-radius:44px}
  .sports-art.left{left:162px;background:linear-gradient(135deg,#d8d8d8,#e8b173)}
  .sports-art.right{left:555px;background:linear-gradient(135deg,#2d5aa6,#e2721f)}
</style>
</head>
<body>
<main class="canvas">
  <div class="ticket-border"></div>
  <div class="ticket-frame"></div>
  <div class="ticket-body"></div>
  <h1 class="invite-heading">YOU ARE INVITED TO</h1>

  <div class="stadium-art" role="img" aria-label="Illustration: graduation stadium with two cheering kids in team helmets, a trophy and sports gear"></div>

  <svg class="decor" viewBox="0 0 805 1200">
    <defs>
      <polygon id="star" points="0,-6 1.8,-1.9 6,-1.9 2.6,0.8 3.7,5 0,2.5 -3.7,5 -2.6,0.8 -6,-1.9 -1.8,-1.9"/>
      <path id="title-arc" d="M141 272 Q 407 222 673 274"/>
      <path id="ribbon-arc" d="M175 600 Q 404 540 650 596"/>
    </defs>
    <g class="star-row">
      <use href="#star" x="150" y="185" fill="var(--navy)"/><use href="#star" x="176" y="185" fill="var(--yellow)"/>
      <use href="#star" x="202" y="185" fill="var(--navy)"/><use href="#star" x="228" y="185" fill="var(--yellow)"/>
      <use href="#star" x="254" y="185" fill="var(--navy)"/><use href="#star" x="280" y="185" fill="var(--yellow)"/>
      <use href="#star" x="306" y="185" fill="var(--navy)"/><use href="#star" x="332" y="185" fill="var(--yellow)"/>
      <use href="#star" x="358" y="185" fill="var(--navy)"/><use href="#star" x="384" y="185" fill="var(--yellow)"/>
      <use href="#star" x="409" y="185" fill="var(--navy)"/><use href="#star" x="435" y="185" fill="var(--yellow)"/>
      <use href="#star" x="461" y="185" fill="var(--navy)"/><use href="#star" x="487" y="185" fill="var(--yellow)"/>
      <use href="#star" x="513" y="185" fill="var(--navy)"/><use href="#star" x="539" y="185" fill="var(--yellow)"/>
      <use href="#star" x="565" y="185" fill="var(--navy)"/><use href="#star" x="591" y="185" fill="var(--yellow)"/>
      <use href="#star" x="617" y="185" fill="var(--navy)"/><use href="#star" x="643" y="185" fill="var(--yellow)"/>
      <use href="#star" x="668" y="185" fill="var(--navy)"/>
    </g>
    <text class="venue-title" font-family="Alfa Slab One, serif" font-size="40" fill="var(--navy)">
      <textPath href="#title-arc" startOffset="50%" text-anchor="middle" textLength="525" lengthAdjust="spacingAndGlyphs">MAPLE CREST STADIUM</textPath>
    </text>
    <path class="event-ribbon" d="M139 563 Q 404 469 679 563 L 655 625 Q 404 545 162 625 Z" fill="var(--yellow)"/>
    <text class="event-name" font-family="Lobster Two, cursive" font-style="italic" font-weight="700" font-size="48" fill="var(--green)">
      <textPath href="#ribbon-arc" startOffset="50%" text-anchor="middle">for the Falcon Trials!</textPath>
    </text>
  </svg>

  <p class="tagline">FOOD, FUN, GAMES &amp; PRIZES AWAIT</p>

  <p class="event-date"><span class="day">JUNE 12</span><span class="year">2020</span></p>
  <span class="year-arrow left"></span>
  <span class="year-arrow right"></span>

  <p class="event-time">6 PM - 9:15 PM</p>

  <p class="arrival-banner">FIFTH GRADERS ARRIVE 6PM</p>

  <p class="parent-note">Parents arrive 8:30 PM for family<br>photos and video presentation</p>

  <div class="sports-art left" role="img" aria-label="Illustration: soccer ball and baseball bat"></div>
  <p class="admit-one">ADMIT ONE</p>
  <div class="sports-art right" role="img" aria-label="Illustration: hockey stick and basketball"></div>
</main>
</body>
</html>
```